Beauty Salon Industry - Web Design Project

zQuarta is a well-funded start up developing an Online Marketing Platform for small businesses in Europe.
We require a large number of high quality business web designs for our business website builder. Our business websites are seamlessly integrated into our Online Marketing systems and therefore it is important for designers to comply with our Design Guidelines.
This is our second contest and it will focus on the beauty salon industry. We will be running contents every 2-3 weeks for a new industry. Last month, we ran a contest for Builder website designs with 3 top prizes (plus £10 per variation) and we also paid out £25 per design for 20+ entries from designers who did not win the top prizes. So we encourage all entries!
We have included a wire frame this time to encourage you to be as creative as possible with your designs and layout while respecting the following guidelines:
1) You CAN change the layout as much as you like. If you think a vertical menu would look better, then use it. If you think the design would benefit from moving an element to a different location, then you can do that too.
2) You must include ALL the elements in the wire frame in your design.(e.g. latest 2 news entries, a testimonial, 1 gallery image, carousel etc...). Please make sure you have looked through the wire frame and know what is required. Entries that do not include all the elements will not qualify to win.
3) So remember, you CAN change the layout as much as you like but DO NOT remove any elements nor move them to a different page.
4) You may change the size and style of the carousel image. We would like to see as many variations of this as possible.
We are rewarding 3 prizes, and would like the winning designer to design the internal pages to the new design.
As always, if we think your designs could be incorporated into our system, but you do not win the competition, we will reward £25. Therefore, we encourage designers to submit as many designs as possible as we may award up to 25 designs.
Judging criteria : -
1) Visual Design
2) Layout must adhere to best practices and wireframe. If you decide to move elements around significantly please provide reason
3) Functional, informative and drives calls to action
Updates
As usual:
1st place = £350
2nd place = £250
3rd place = £150
Good luck!
Very happy with all the designs submitted so far, and will provide feedback ASAP.
We would like to see you try arranging the elements differently. So please try different navigation types and layouts.
Thanks
Morris
Prize funds for 1st place has been slightly increased.
Thanks
Morris
We have already had some amazing designs submitted. Thanks.
Remember to play with the layout of the elements and try designs with a carousel/slider that is in portrait not just in landscape.
Thanks everyone!
Morris
Hi everyone, we are really enjoying looking through the designs.
We have one NEW requirement. If you have used an image from http://www.frelik-example.com/ in your design, could you please replace it with another.
We are not associated with them.
Thank you.
I have just sent a poll around the office to vote on all the designs and hope to have the results soon.
Good luck and I hope to see all your great designs for our next project in a couple of weeks.
Morris
Hi everyone, we hope you have had a good holiday season. We will be rewarding the prizes very soon, hopefully today or tomorrow.
Thanks
Morris
We are currently going through all the designs that did not win our competition and will be contacting the designers of the designs we would like to use in our system, so please keep an eye on your inbox over the next few days.
Thank you
Morris
Target Market(s)
Beauty Salon Industry
Industry/Entity Type
Beauty Salon
Look and feel
Each slider illustrates characteristics of the customer's brand and the style your logo design should communicate.

```html
<!DOCTYPE html>
<html lang="en">
<head>
<meta charset="utf-8">
<title>Silk Breeze – Hair and urban spa</title>
<link rel="stylesheet" href="https://fonts.googleapis.com/css2?family=Ubuntu:ital,wght@0,400;0,500;0,700;1,500&family=Noto+Serif:ital@1&display=swap">
<style>
:root{
  --green:#5b6f1a;
  --green-dark:#4d5f14;
  --green-mid:#7c9a2b;
  --green-pale:#c9dc8c;
  --lime:#d7ec6a;
  --pink:#ee1a7c;
  --orange:#f08a1c;
  --ink:#222;
  --grey:#dcdcdc;
  --grey-line:#bfbfbf;
  --text:#333;
}
*{margin:0;padding:0;box-sizing:border-box}
html,body{width:1200px;height:1170px;overflow:hidden}
body{position:relative;font-family:"Ubuntu",sans-serif;color:var(--text);
  background:linear-gradient(180deg,#eceeec 0,#f6f7f6 480px,#fff 700px)}
.abs{position:absolute}
a{color:inherit}

.header{left:0;top:0;width:1200px;height:106px;background:linear-gradient(90deg,var(--green) 0,#63781f 60%,#6a8024 100%)}
.brand{left:126px;top:26px;color:#f1f1e4}
.brand-name{font-size:40px;font-weight:400;letter-spacing:1px;line-height:40px}
.brand-tag{display:block;text-align:right;font-size:12px;margin-top:2px}
.phone{left:840px;top:42px;color:#fff;font-size:27px;font-weight:500;display:flex;align-items:center;gap:10px}
.book-now{left:930px;top:79px;width:124px;height:33px;border-radius:5px;border:2px solid #e5f0b0;z-index:5;
  background:linear-gradient(#c4dd5e,#8fae27);color:#203005;font-size:19px;font-weight:500;text-align:center;line-height:29px}

.nav{left:121px;top:105px;width:960px;height:35px;background:var(--green);border-radius:0 0 10px 10px;display:flex;align-items:center;padding-left:4px;z-index:1}
.nav a{color:#fff;text-decoration:none;font-size:14px;padding:0 20px;border-right:1px solid #7a8e3a}
.nav a:last-child{border:none}

.hero{left:122px;top:148px;width:648px;height:321px;border:6px solid var(--green-pale);background:#fff}
.hero-photo{position:absolute;inset:1px;background:radial-gradient(ellipse at 60% 45%,#8a4a2b 0,#b46a45 25%,#f3ebe6 55%,#fbf8f6 100%)}
.hero-arrows{position:absolute;left:545px;top:262px;display:flex;gap:10px}

.promo{left:778px;top:148px;width:302px;height:196px;border:2px solid var(--orange);
  background:linear-gradient(180deg,#f5a33a 0,#e7821c 45%,#c3341a 100%)}
.promo-price{position:absolute;left:9px;top:12px;font-size:36px;font-weight:700;color:#1a0d00}
.promo-note{position:absolute;left:9px;top:56px;font-size:14px;font-weight:500;color:#1a0d00}
.promo-btn{position:absolute;left:7px;top:83px;width:286px;height:35px;border-radius:7px;background:linear-gradient(#444,#000);
  color:#fff;font-size:18px;font-weight:500;text-align:center;line-height:35px}
.promo-img{position:absolute;left:0;right:0;top:128px;bottom:0;background:linear-gradient(180deg,#d96a26,#a3261a)}

.info{left:778px;top:352px;width:299px;height:118px;background:#e3e3e3;border:1px solid var(--grey-line)}
.info h3{font-size:15px;font-weight:500;color:var(--green)}
.addr{position:absolute;left:10px;top:7px}
.addr p{margin:6px 0 0 15px;font-size:14px;line-height:18px;color:#222}
.addr a{display:block;margin:6px 0 0 13px;font-size:13px;color:var(--green)}
.hours{position:absolute;left:150px;top:7px}
.hours ul{list-style:none;margin:5px 0 0 10px;font-size:11px;line-height:14px;color:#222}

.intro{left:120px;top:483px;width:303px;height:460px;background:var(--pink);border-radius:45px 0 0 0;color:#fff;overflow:hidden}
.intro h2{margin:20px 12px 0;text-align:center;font-size:19px;font-weight:500;line-height:24px;text-transform:uppercase}
.intro p{margin:16px 6px 0 12px;font-size:12.5px;line-height:18px}
.intro .more{position:absolute;right:6px;top:225px;font-size:12px;color:#ffe06a}
.intro-photo{position:absolute;left:0;top:246px;width:303px;height:214px;background:linear-gradient(160deg,#2f7a2c 0,#b6a88b 45%,#d9c9a4 70%,#7a5b36 100%)}

.quote{left:432px;top:481px;width:646px;height:96px;border:1px solid #cfcfcf;border-radius:12px;background:linear-gradient(#fff,#ebebeb)}
.quote blockquote{position:absolute;left:16px;top:21px;width:616px;font-family:"Noto Serif",serif;font-style:italic;font-size:13.5px;letter-spacing:-0.3px;line-height:22px;color:#555}
.quote blockquote a{color:var(--pink)}
.quote cite{position:absolute;right:22px;top:58px;font-style:italic;font-weight:500;font-size:15px;color:#222}

.news{left:438px;top:594px;width:322px}
.news h2{font-size:20px;font-weight:500;color:var(--green);line-height:26px}
.news article{position:relative;padding:8px 2px 10px;border-bottom:1px dotted #999;font-size:12.5px;line-height:20px;color:#222}
.news article p{width:300px}
.news time{color:var(--pink);display:block;line-height:20px;margin-bottom:2px}
.news .more{position:absolute;right:10px;top:52px;font-size:11px;color:var(--pink)}
.news article:last-of-type{border:none;padding-bottom:0}
.news .all{display:block;margin:2px 0 0 2px;font-size:11px;color:var(--pink)}

.xmas{left:786px;top:597px;width:293px;height:201px;border:2px solid #cfcfcf;
  background:radial-gradient(ellipse at 70% 40%,#fbf3bd 0,#efdc7a 55%,#d8b43c 100%);overflow:hidden}
.xmas h3{position:absolute;left:11px;top:9px;font-size:19px;font-weight:500;color:#111}
.xmas p{position:absolute;left:11px;top:41px;width:275px;font-size:12.5px;line-height:20px;color:#222}
.xmas-gift{position:absolute;left:0;top:120px;width:150px;height:80px;background:linear-gradient(90deg,#c82a1a,#e6b64a)}
.xmas strong{position:absolute;font-size:24px;font-weight:500;color:#111;line-height:28px}

.rule{left:440px;top:830px;width:635px;border-top:1px dotted #999}
.partners{left:432px;top:857px;display:flex;gap:6px}
.partners div{width:158px;height:87px;background:var(--grey);border:1px solid var(--grey-line);display:flex;align-items:center;justify-content:center;font-size:24px;color:#111}

.footer{left:0;top:977px;width:1200px;height:161px;background:linear-gradient(90deg,#5d721c,#647a22)}
.gallery{left:124px;top:961px;width:286px;height:190px;background:var(--green-mid);border:3px solid #a7bf56}
.gallery-tab{position:absolute;left:15px;top:21px;width:50px;height:142px;background:var(--green-dark);border-radius:10px 0 0 10px;
  color:#fff;font-size:22px;font-weight:500;writing-mode:vertical-rl;transform:rotate(180deg);display:flex;align-items:center;justify-content:center;letter-spacing:1px}
.gallery-photo{position:absolute;left:62px;top:7px;width:212px;height:170px;border:3px solid #fff;background:linear-gradient(160deg,#5a5a5a,#d8c0a8 50%,#f2e4d4)}
.foot-nav{right:126px;top:994px;font-size:13px;color:#fff}
.foot-nav a{text-decoration:none;color:#fff}
.foot-nav span{margin:0 13px}
.admin{right:126px;top:1032px;font-size:13px;color:var(--lime)}
.managed{right:128px;top:1090px;font-size:11.5px;color:#d5dcb8}
.copy{right:128px;top:1112px;font-size:11.5px;color:#d5dcb8}
</style>
</head>
<body>

<header class="header abs"></header>
<div class="brand abs"><span class="brand-name">SILK BREEZE</span><span class="brand-tag">Hair and urban spa</span></div>
<div class="phone abs">
  <svg width="24" height="24" viewBox="0 0 24 24"><rect width="24" height="24" rx="4" fill="#a7c24a"/><path d="M8 5c1 0 2 3 2 4s-1 1-1 2 2 4 4 4 1-1 2-1 4 1 4 2-2 3-3 3C9 19 5 12 5 8c0-1 2-3 3-3z" fill="#4a5e12"/></svg>
  020 7946 0312
</div>

<nav class="nav abs">
  <a href="#">Home</a><a href="#">Services</a><a href="#">Gallery</a><a href="#">Testimonials</a><a href="#">News</a><a href="#">About Us</a><a href="#">Contact Us</a>
</nav>
<div class="book-now abs">Book Now</div>

<section class="hero abs">
  <div class="hero-photo" role="img" aria-label="Carousel photo: woman with long auburn hair among flowers and candles"></div>
  <div class="hero-arrows">
    <svg width="38" height="38" viewBox="0 0 38 38"><circle cx="19" cy="19" r="17" fill="#f2f2f2" stroke="#999" stroke-width="2"/><path d="M22 11l-8 8 8 8" fill="none" stroke="#444" stroke-width="3"/></svg>
    <svg width="38" height="38" viewBox="0 0 38 38"><circle cx="19" cy="19" r="17" fill="#f2f2f2" stroke="#999" stroke-width="2"/><path d="M16 11l8 8-8 8" fill="none" stroke="#444" stroke-width="3"/></svg>
  </div>
</section>

<aside class="promo abs">
  <div class="promo-img" role="img" aria-label="Wrapped red gift boxes with gold ribbon"></div>
  <div class="promo-price">$25</div>
  <div class="promo-note">Complimentary gift for first time clients!</div>
  <div class="promo-btn">BOOK APPOINTMENT NOW</div>
</aside>

<section class="info abs">
  <div class="addr">
    <h3>Frelik Address</h3>
    <p>12 Linden Row<br>London<br>W1X 4QQ</p>
    <a href="#">view map</a>
  </div>
  <div class="hours">
    <h3>Business Hours</h3>
    <ul><li>Mon. 9 am - 5pm</li><li>Tue 9 am - 5pm</li><li>Wed 9 am - 5pm</li><li>Thu 9 am - 5pm</li><li>Fri 9 am - 5pm</li><li>Sat 9 am - 5pm</li></ul>
  </div>
</section>

<section class="intro abs">
  <h2>Let our hair and beauty skills blow you away</h2>
  <p>Silk Breeze is a passionate, creative team, dedicated to none, personal salon experience that will blow your mind.</p>
  <p>Where ultimate hairdressing comes hand-in-hand with style, glamour, fashion, innovation and skill to create an exquisite salon experience in the heart of london.</p>
  <a class="more" href="#">read more</a>
  <div class="intro-photo" role="img" aria-label="Spa stones, leaves, towel and lit candles"></div>
</section>

<section class="quote abs">
  <blockquote>My hairstylist, Marisol, was truly amazing. she listened to exactly what i wanted, but also told me exactly what... <a href="#">more</a></blockquote>
  <cite>- Talia Brennan</cite>
</section>

<section class="news abs">
  <h2>What to be a hair model?</h2>
  <article><time>9 Nov 2011</time><p>We always need models for our portfolio If you want to become one please contact us.</p><a class="more" href="#">more</a></article>
  <article><time>9 Nov 2011</time><p>We always need models for our portfolio If you want to become one please contact us.</p><a class="more" href="#">more</a></article>
  <a class="all" href="#">more news</a>
</section>

<aside class="xmas abs">
  <div class="xmas-gift" role="img" aria-label="Red gift with gold bow"></div>
  <h3>Book Now for Christmas</h3>
  <p>Our salon is usually very busy for the two weeks before christmas, so please book early:</p>
  <strong style="left:6px;top:98px">Call 020 7946 0312,</strong>
  <strong style="right:11px;top:127px">or Contact us</strong>
</aside>

<div class="rule abs"></div>
<section class="partners abs">
  <div>Lumora</div><div>Vessa</div><div style="font-size:16px">Fern and fern</div><div>Kaltrin</div>
</section>

<footer class="footer abs"></footer>
<section class="gallery abs">
  <div class="gallery-tab">GALLERY</div>
  <div class="gallery-photo" role="img" aria-label="Client having her hair washed at a salon basin"></div>
</section>
<nav class="foot-nav abs">
  <a href="#">Home</a><span>|</span><a href="#">Services</a><span>|</span><a href="#">Gallery</a><span>|</span><a href="#">Testimonials</a><span>|</span><a href="#">News</a><span>|</span><a href="#">About Us</a><span>|</span><a href="#">Contact Us</a>
</nav>
<a class="admin abs" href="#">Admin</a>
<div class="managed abs">Managed by zquarta.com</div>
<div class="copy abs">Copyright@ 2011 All Rights Reserved.</div>

</body>
</html>
```